Pause Your Day And Browse- PYDB poster

I am the Vice President of Advocacy for the Coastline Shelfkeepers Guild. I am looking to have a set of posters made for PYDB (Pause Your Day and Browse) October 23. PYDB is a time when all school children in BC are encouraged to Pause Your Day and Browse for 15-20 minutes at some point in their day.

I would like to get a set of 2 digital posters designed (if possible it would be nice to have the option to print to both 11 x 17 and 8.5 x 11 paper). We need a poster that is high school (Grade 8-12) appropriate and one that is elementary (Grade k-7) appropriate. Both posters need to be replicated in French. All posters need to have the KWNU logo on them as well as the Coastline Shelfkeepers Guild Logo.

Here is a link to last year's successful design http://kwnu-example.org/csg/info/advocacy.html
There are two additional samples in the uploaded files section.

Each poster needs to have the following information:

-Pause Your Day and Browse (PYDB)
- The date Monday, October 23, 2017
-the logo for the KWNU (attached)
-the logo for the CSG (attached)- the logos do not have to be large.

Target Market(s)

Children ages 5-12 and 12-17 as well as their teachers

Industry/Entity Type

Teacher

Font styles to use
Sans Serif

Requirements
Must have
• Must have both logos- colours may be changed for either or both
Nice to have
• Clear, Bright lettering. Images of child or children enjoying reading
Should not have
• stereotypes

```html
<!DOCTYPE html>
<html lang="en">
<head>
<meta charset="utf-8">
<title>PYDB – Pause Your Day and Browse</title>
<link href="https://fonts.googleapis.com/css2?family=Barlow:wght@600;700&display=swap" rel="stylesheet">
<style>
  :root {
    --pink: #e8386f;
    --pink-mid: #ec5c86;
    --pink-light: #f5b3c6;
    --blush: #f8dfe6;
    --glow: #fdf4f4;
    --page: #f4f1ee;
    --rose-top: #f2a6bd;
    --berry: #d8405e;
    --carpet: #c7b59c;
    --carpet-dark: #8f7f68;
    --yellow: #ffcc00;
    --white: #ffffff;
  }
  * { margin: 0; padding: 0; box-sizing: border-box; }
  html, body { width: 1200px; height: 927px; overflow: hidden; background: var(--pink); }
  .poster {
    position: relative;
    width: 1200px;
    height: 927px;
    overflow: hidden;
    background: var(--pink);
    font-family: "Barlow", "Arial", sans-serif;
  }

  .reading-photo {
    position: absolute;
    inset: 0;
    background:
      linear-gradient(to right, var(--pink) 0%, var(--pink) 30%, rgba(232,56,111,0.55) 44%, rgba(232,56,111,0) 60%),
      radial-gradient(ellipse 170px 80px at 1020px 150px, var(--glow) 0%, rgba(253,244,244,0) 100%),
      radial-gradient(ellipse 240px 60px at 900px 330px, rgba(255,255,255,0.75) 0%, rgba(255,255,255,0) 100%),
      radial-gradient(ellipse 130px 120px at 905px 300px, rgba(240,200,180,0.55) 0%, rgba(240,200,180,0) 100%),
      radial-gradient(ellipse 230px 150px at 905px 520px, var(--rose-top) 0%, rgba(242,166,189,0) 100%),
      radial-gradient(ellipse 300px 90px at 920px 640px, var(--page) 0%, rgba(244,241,238,0) 100%),
      radial-gradient(ellipse 340px 110px at 930px 760px, var(--blush) 0%, rgba(248,223,230,0) 100%),
      radial-gradient(ellipse 150px 150px at 390px 760px, rgba(216,64,94,0.7) 0%, rgba(216,64,94,0) 100%),
      linear-gradient(to bottom, rgba(199,181,156,0) 80%, var(--carpet) 92%, var(--carpet-dark) 100%),
      linear-gradient(to right, var(--pink-mid) 0%, var(--pink-light) 50%, var(--blush) 100%);
  }

  .headline { position: absolute; left: 40px; top: 58px; color: var(--yellow); font-weight: 700; line-height: 1; }
  .acronym { display: block; font-size: 236px; letter-spacing: 2px; }
  .title { display: block; margin-top: 2px; }
  .title-top { display: block; font-size: 62px; letter-spacing: 1px; }
  .title-bottom { display: block; font-size: 122px; margin-top: -6px; }

  .event-date {
    position: absolute; left: 42px; top: 494px;
    color: var(--white); font-size: 50px; font-weight: 700; line-height: 1;
  }

  .partner {
    position: absolute; display: flex; align-items: center; gap: 12px;
    color: var(--white); font-weight: 700; line-height: 1; font-size: 52px;
  }
  .partner-guild { left: 42px; top: 796px; }
  .partner-guild .mark { width: 40px; height: 40px; background: var(--white); }
  .partner-union { left: 242px; top: 796px; }
  .partner-union .mark { width: 40px; height: 40px; border-radius: 50%; background: var(--white); }
</style>
</head>
<body>
  <main class="poster">
    <div class="reading-photo" role="img" aria-label="Photo of a smiling young girl in pink sitting cross-legged on a carpet, reading a large open book in a sunny pink bedroom with a lamp, a shelf and a teddy bear"></div>

    <h1 class="headline">
      <span class="acronym">PYDB</span>
      <span class="title">
        <span class="title-top">PAUSE YOUR DAY</span>
        <span class="title-bottom">AND BROWSE</span>
      </span>
    </h1>

    <p class="event-date">Monday, October 23, 2017</p>

    <div class="partner partner-guild"><span class="mark"></span><span>CSG</span></div>
    <div class="partner partner-union"><span class="mark"></span><span>KWNU</span></div>
  </main>
</body>
</html>
```